ROVA Pty Ltd Business Card

Looking for a simple yet eye-catching double-sided business card design using my company logo on one side and contact details on the other.

Target Market(s)

Government

Industry/Entity Type

Communication Systems Engineering

Contact Information for Business Card

ROVA Pty Ltd

Requirements
Nice to have
• Would be great to have a QR code so details can be scanned into contacts

```html
<!DOCTYPE html>
<html lang="en">
<head>
<meta charset="utf-8">
<title>ROVA Pty Ltd Business Card</title>
<link rel="stylesheet" href="https://fonts.googleapis.com/css2?family=Montserrat:wght@500;600&family=Questrial&display=swap">
<style>
  :root {
    --backdrop: #79b5f1;
    --card-white: #ffffff;
    --panel-dark: #2b2b2b;
    --accent-grey: #58534f;
    --accent-orange: #f07a2b;
    --ink: #111111;
    --brand-slate: #37424a;
    --card-shadow: 0 14px 28px rgba(20, 50, 90, 0.45);
  }
  * { margin: 0; padding: 0; box-sizing: border-box; }
  html, body {
    width: 1200px;
    height: 1200px;
    overflow: hidden;
    background: var(--backdrop);
  }
  .card {
    position: absolute;
    left: 173px;
    width: 854px;
    height: 512px;
    background: var(--card-white);
    box-shadow: var(--card-shadow);
    overflow: hidden;
  }
  .card--front { top: 70px; }
  .card--back { top: 624px; }

  .brand-panel {
    position: absolute;
    left: 0; top: 0;
    width: 409px; height: 100%;
    background: var(--panel-dark);
    display: flex;
    align-items: center;
    justify-content: center;
  }
  .brand-name {
    font-family: "Montserrat", sans-serif;
    font-weight: 600;
    letter-spacing: 4px;
    line-height: 1;
  }
  .brand-panel .brand-name {
    color: var(--card-white);
    font-size: 66px;
  }

  .corner-bar {
    position: absolute;
    right: 0; top: 0;
    width: 37px; height: 176px;
    background: var(--accent-grey);
  }
  .icon-bar {
    position: absolute;
    left: 409px; top: 270px;
    width: 37px; height: 242px;
    background: var(--accent-grey);
  }

  .identity {
    position: absolute;
    right: 57px; top: 80px;
    text-align: right;
    font-family: "Montserrat", sans-serif;
    font-weight: 500;
  }
  .identity__name {
    font-size: 40px;
    letter-spacing: 3px;
    color: var(--ink);
    line-height: 1.1;
  }
  .identity__name .surname { color: var(--accent-orange); }
  .identity__title {
    font-size: 25px;
    letter-spacing: 2px;
    color: var(--ink);
    margin-top: 2px;
  }

  .contact-row {
    position: absolute;
    left: 409px;
    display: flex;
    align-items: center;
    font-family: "Questrial", sans-serif;
    color: var(--ink);
  }
  .contact-row__icon {
    width: 37px;
    display: flex;
    justify-content: center;
  }
  .contact-row__text {
    margin-left: 23px;
    font-size: 24px;
    line-height: 1.2;
  }
  .contact-row--phone { top: 298px; }
  .contact-row--email { top: 350px; }
  .contact-row--address { top: 392px; align-items: flex-start; }
  .contact-row--address .contact-row__icon { padding-top: 3px; }
  .contact-row--address .contact-row__text { font-size: 19px; line-height: 1.25; }

  .back-brand {
    position: absolute;
    left: 0; right: 0; top: 160px;
    display: flex;
    justify-content: center;
  }
  .back-brand .brand-name {
    color: var(--brand-slate);
    font-size: 80px;
    letter-spacing: 6px;
  }
  .website {
    position: absolute;
    left: 0; right: 0; top: 430px;
    text-align: center;
    font-family: "Questrial", sans-serif;
    font-size: 22px;
    color: var(--ink);
  }
</style>
</head>
<body>
  <section class="card card--front" aria-label="Business card front">
    <div class="brand-panel">
      <span class="brand-name">ROVA</span>
    </div>
    <div class="corner-bar"></div>
    <div class="icon-bar"></div>

    <div class="identity">
      <p class="identity__name">LIAM <span class="surname">CARTER</span></p>
      <p class="identity__title">CEO DIRECTOR</p>
    </div>

    <div class="contact-row contact-row--phone">
      <span class="contact-row__icon">
        <svg width="18" height="18" viewBox="0 0 24 24" aria-hidden="true"><path fill="#fff" d="M6.6 10.8a15.1 15.1 0 0 0 6.6 6.6l2.2-2.2c.3-.3.7-.4 1-.2 1.1.4 2.3.6 3.6.6.6 0 1 .4 1 1V20c0 .6-.4 1-1 1A17 17 0 0 1 3 4c0-.6.4-1 1-1h3.5c.6 0 1 .4 1 1 0 1.3.2 2.5.6 3.6.1.3 0 .7-.2 1z"/></svg>
      </span>
      <span class="contact-row__text">+000 987-654-321</span>
    </div>
    <div class="contact-row contact-row--email">
      <span class="contact-row__icon">
        <svg width="20" height="16" viewBox="0 0 20 16" aria-hidden="true"><rect x="1" y="1" width="18" height="14" fill="none" stroke="#fff" stroke-width="2"/><path d="M1 1l9 8 9-8" fill="none" stroke="#fff" stroke-width="2"/></svg>
      </span>
      <span class="contact-row__text">admin@rova.com.au</span>
    </div>
    <div class="contact-row contact-row--address">
      <span class="contact-row__icon">
        <svg width="20" height="18" viewBox="0 0 20 18" aria-hidden="true"><path fill="#fff" d="M10 0l10 9h-3v9h-5v-6H8v6H3V9H0z"/></svg>
      </span>
      <span class="contact-row__text">42-44 Harbour Lane Pyrmont<br>NSW 2009 Australia</span>
    </div>
  </section>

  <section class="card card--back" aria-label="Business card back">
    <div class="back-brand">
      <span class="brand-name">ROVA</span>
    </div>
    <p class="website">rova.com.au</p>
  </section>
</body>
</html>
```